Business Card Design Project

I need a new business card design for my Remodel/Design/Build company, Brightfield Renovation Works, Inc. See our website: www.brightfieldrenovationworks.com
We are an established company with a growing reputation and growing quickly. We are know for being on the forward edge of the industry, producing a great product and our "people friendly" approach.
I am looking for something cool, transitional, maybe even retro that captures the imagination, shows our sleek creativity and streamlined approach as well as communicates stability and trustworthiness.
Updates

Stainless steel business card design would be cool.

Please have all future designs with full logo colors and shown on a stainless steel business card.  Also, logo and tag line will most likely be printed with spot uv, so layers will be necessary.  Thank you.

Target Market(s)

30-65 yrs old, homeowners, appreciate fine things, median income $150+k, net worth $1+m

Industry/Entity Type

Business

Requirements
Must have
• Company Logo
Contact information
Website URL
Nice to have
• Tagline: Building Relationships and Remodeling Homes...One Client at a Time.
Double-sided okay.
Stainless steel business card.

```html
<!DOCTYPE html>
<html lang="en">
<head>
<meta charset="utf-8">
<title>Brightfield Renovation Works – Business Card</title>
<link rel="stylesheet" href="https://fonts.googleapis.com/css2?family=Didact+Gothic&display=swap">
<style>
  :root {
    --backdrop: #e4e2df;
    --steel-light: #f4f4f4;
    --steel-mid: #d2d2d2;
    --steel-dark: #a9a9a9;
    --card-edge: #2b2b2b;
    --brand-red: #7a161b;
    --tagline-ink: #2a2a2a;
  }
  * { margin: 0; padding: 0; box-sizing: border-box; }
  html, body {
    width: 1200px;
    height: 724px;
    overflow: hidden;
    background: var(--backdrop);
    font-family: "Didact Gothic", "Century Gothic", sans-serif;
  }
  .card {
    position: absolute;
    left: 30px;
    top: 30px;
    width: 1140px;
    height: 664px;
    border-radius: 48px;
    border: 3px solid var(--card-edge);
    overflow: hidden;
    background:
      radial-gradient(ellipse at 55% 55%, rgba(255,255,255,0.75) 0%, rgba(255,255,255,0) 45%),
      repeating-conic-gradient(from 0deg at 55% 55%,
        var(--steel-light) 0deg 4deg,
        var(--steel-mid) 9deg,
        var(--steel-light) 14deg 20deg,
        var(--steel-dark) 30deg,
        var(--steel-light) 45deg);
  }
  .brand {
    position: absolute;
    left: 150px;
    top: 110px;
    display: flex;
    align-items: center;
    gap: 44px;
  }
  .brand-mark {
    width: 230px;
    height: 230px;
    flex: none;
  }
  .brand-name {
    color: var(--brand-red);
    font-size: 60px;
    font-weight: 400;
    letter-spacing: 0.06em;
    line-height: 1.15;
    text-transform: uppercase;
  }
  .tagline {
    position: absolute;
    left: 0;
    right: 0;
    top: 500px;
    text-align: center;
    color: var(--tagline-ink);
    font-size: 32px;
    line-height: 1.5;
  }
</style>
</head>
<body>
  <main class="card">
    <div class="brand">
      <svg class="brand-mark" viewBox="0 0 230 230" aria-hidden="true">
        <circle cx="115" cy="115" r="112" fill="var(--brand-red)"/>
      </svg>
      <h1 class="brand-name">Brightfield<br>Renovation Works</h1>
    </div>
    <p class="tagline">Building Relationships and Remodeling Homes...<br>One Client at a Time</p>
  </main>
</body>
</html>
```